New Business Card Design

We need a business card design for a new company based in Sydney called "Hearth and Ember". This is an online buisness which will have an online store providing imported homewares.
We are looking for something that is different, perhaps even in shape and using the logo that was designed by Pixel Meadow.

Attached document is a basic example I want to see more creative versions.

Target Market(s)

Homewares, Interior Design

Industry/Entity Type

Business

Contact Information for Business Card

Company Logo
Company Name
Industry area
Name
Position
Phone
Email
Website
Motto

Requirements
Must have
• Logo
Nice to have
• Social website logos - Friendlane, Glimmerly, Quipster, Boardwhim, Zumvo+

```html
<!DOCTYPE html>
<html lang="en">
<head>
<meta charset="utf-8">
<title>Hearth and Ember – Business Card</title>
<link href="https://fonts.googleapis.com/css2?family=Montserrat:wght@400;600&family=Open+Sans:wght@400&family=Roboto+Condensed:wght@700&family=Great+Vibes&display=swap" rel="stylesheet">
<style>
  :root {
    --backdrop: #a9a7a7;
    --card: #fdfdfc;
    --ink: #1c1c1c;
    --ink-soft: #2a2a2a;
    --tan: #b48a64;
    --gold-1: #b07a2e;
    --gold-2: #f4dc9e;
    --gold-3: #d7ac5a;
    --bronze: #6e3a26;
    --black: #1a1a1a;
  }
  * { margin: 0; padding: 0; box-sizing: border-box; }
  html, body { width: 1200px; height: 1200px; overflow: hidden; }
  body {
    background: var(--backdrop);
    position: relative;
    font-family: "Open Sans", sans-serif;
    color: var(--ink);
  }
  .card {
    position: absolute;
    width: 712px;
    height: 417px;
    background: var(--card);
    border-radius: 28px;
    overflow: hidden;
  }
  .card--front { left: 238px; top: 120px; }
  .card--back  { left: 231px; top: 645px; }

  .card-band { position: absolute; left: 0; bottom: 0; }

  /* Front */
  .front-mark {
    position: absolute; left: 0; right: 0; top: 128px;
    display: flex; justify-content: center; align-items: center; gap: 16px;
    font-family: "Montserrat", sans-serif; font-weight: 600;
    font-size: 46px; color: var(--ink);
  }
  .front-mark .dot {
    width: 22px; height: 22px; border-radius: 50%; background: var(--gold-3);
  }
  .front-industry {
    position: absolute; left: 0; right: 0; top: 288px; text-align: center;
    font-family: "Montserrat", sans-serif; font-weight: 400;
    font-size: 37px; letter-spacing: 4px; color: var(--ink);
  }
  .front-web {
    position: absolute; left: 0; right: 0; top: 340px;
    display: flex; justify-content: center; align-items: center; gap: 10px;
    font-size: 17px; color: var(--ink-soft);
  }
  .front-web .rule {
    width: 90px; height: 3px;
    background: linear-gradient(90deg, transparent, var(--gold-1) 40%, var(--bronze));
  }
  .front-web .rule--right { transform: scaleX(-1); }

  /* Back */
  .back-mark {
    position: absolute; left: 50px; width: 254px; top: 86px;
    text-align: center;
    font-family: "Montserrat", sans-serif; font-weight: 600;
    font-size: 25px; color: var(--ink);
  }
  .brand-name {
    position: absolute; left: 50px; width: 254px; top: 186px; text-align: center;
    font-family: "Montserrat", sans-serif; font-weight: 600; font-size: 22px;
  }
  .brand-industry {
    position: absolute; left: 50px; width: 254px; top: 215px; text-align: center;
    font-family: "Montserrat", sans-serif; font-size: 17px; letter-spacing: 2px;
  }
  .social-list { position: absolute; left: 45px; top: 263px; list-style: none; }
  .social-list li {
    display: flex; align-items: center; gap: 14px;
    height: 25.5px; font-size: 17px; color: var(--ink-soft);
  }
  .social-list .badge { width: 16px; height: 16px; border-radius: 3px; background: var(--tan); }

  .person-name {
    position: absolute; left: 373px; top: 64px;
    font-family: "Roboto Condensed", sans-serif; font-weight: 700;
    font-size: 28px; color: var(--tan);
  }
  .person-role { position: absolute; left: 373px; top: 106px; font-size: 16px; color: var(--ink-soft); }

  .contact-list { position: absolute; left: 372px; top: 197px; list-style: none; }
  .contact-list li {
    display: flex; align-items: center; gap: 14px;
    height: 30px; font-size: 17px; color: var(--ink-soft);
  }
  .contact-list svg { width: 18px; height: 18px; fill: var(--tan); }

  .motto {
    position: absolute; right: 60px; bottom: 10px;
    font-family: "Great Vibes", cursive; font-size: 28px; color: #fff8ea;
  }
</style>
</head>
<body>

<section class="card card--front" aria-label="Card front">
  <div class="front-mark"><span class="dot"></span>Hearth and Ember</div>
  <div class="front-industry">HOMEWARES</div>
  <div class="front-web"><span class="rule"></span>www.hearthandember.com.au<span class="rule rule--right"></span></div>
  <svg class="card-band" width="712" height="20" viewBox="0 0 712 20">
    <defs>
      <linearGradient id="frontGold" x1="0" x2="1">
        <stop offset="0" stop-color="var(--gold-1)"/>
        <stop offset="0.22" stop-color="var(--gold-2)"/>
        <stop offset="0.5" stop-color="var(--bronze)"/>
        <stop offset="0.75" stop-color="var(--gold-3)"/>
        <stop offset="0.9" stop-color="var(--gold-2)"/>
        <stop offset="1" stop-color="var(--gold-1)"/>
      </linearGradient>
    </defs>
    <rect x="0" y="0" width="712" height="20" fill="var(--black)"/>
    <polygon points="0,0 505,0 475,20 0,20" fill="url(#frontGold)"/>
  </svg>
</section>

<section class="card card--back" aria-label="Card back">
  <div class="back-mark">Hearth and Ember</div>
  <div class="brand-name">Hearth and Ember</div>
  <div class="brand-industry">HOMEWARES</div>
  <ul class="social-list">
    <li><span class="badge"></span>hearthandember</li>
    <li><span class="badge"></span>hearthandember</li>
    <li><span class="badge"></span>@HearthAndEmber1</li>
    <li><span class="badge"></span>hearthandemberhomewares</li>
  </ul>

  <div class="person-name">Lucia Moreno Hale</div>
  <div class="person-role">Director / Designer</div>

  <ul class="contact-list">
    <li>
      <svg viewBox="0 0 20 20" aria-hidden="true"><path d="M3 7c0-2 3-4 7-4s7 2 7 4v1h-4V6.5H7V8H3z"/><rect x="4" y="10" width="12" height="7" rx="1"/></svg>
      +61 400 555 019
    </li>
    <li>
      <svg viewBox="0 0 20 20" aria-hidden="true"><path d="M2 5h16v10H2z M3 6l7 5 7-5" fill="var(--tan)" stroke="var(--card)" stroke-width="1.2"/></svg>
      Lucia@hearthandember.com.au
    </li>
    <li>
      <svg viewBox="0 0 20 20" aria-hidden="true"><circle cx="10" cy="10" r="8"/><path d="M2 10h16M10 2c-3 3-3 13 0 16M10 2c3 3 3 13 0 16" fill="none" stroke="var(--card)" stroke-width="1.1"/></svg>
      www.hearthandember.com.au
    </li>
  </ul>

  <svg class="card-band" width="712" height="52" viewBox="0 0 712 52">
    <defs>
      <linearGradient id="backGold" x1="0" x2="1">
        <stop offset="0" stop-color="var(--gold-3)"/>
        <stop offset="0.3" stop-color="var(--gold-2)"/>
        <stop offset="0.7" stop-color="var(--gold-1)"/>
        <stop offset="1" stop-color="var(--bronze)"/>
      </linearGradient>
    </defs>
    <polygon points="0,25 330,25 310,52 0,52" fill="var(--black)"/>
    <polygon points="338,0 712,0 712,52 305,52" fill="url(#backGold)"/>
  </svg>
  <div class="motto">Adding Style to your Home</div>
</section>

</body>
</html>
```